Quandoria Tours - Astronomy in the Kimberley

Quandoria Tours requires a web page to advertise astronomy tours in the East Kimberley, Australia. It needs the following tabs - Home, Tours, Astronomy Events, Gallery, Testimonials, Contacts.

It should target tourists to the Kimberley.
We are unsure of which colours to go with at the moment but we have included our logo if it helps.

It should be mobile and tablet friendly.

Target Market(s)

Families, +40, Tourist, hobby astronomists,

Industry/Entity Type

Events

Number of Pages Required

3 page

Colors
3377b5
ffffff

Requirements
Must have
• Home, Tours, Astronomy Events, Gallery, Calendar, Testimonials, Contacts.
• 'Quandoria Tours' logo
Nice to have
• Pictures of portable amateur telescopes. Pictures of Lake Kununurra or Wyndham.
Should not have
• Pictures of extremely large professional telescopes.

```html
<!DOCTYPE html>
<html lang="en">
<head>
<meta charset="utf-8">
<title>Quandoria Tours - Astronomy in the Kimberley</title>
<link rel="stylesheet" href="https://fonts.googleapis.com/css2?family=Exo+2:wght@300;400;500;600;700&family=Open+Sans:wght@400;600&display=swap">
<style>
:root{
  --blue:#3377b5;
  --blue-btn:#2b63ae;
  --blue-deep:#2a5a98;
  --navy:#1d2f4c;
  --white:#ffffff;
  --ink:#2b2b2b;
  --grey:#8a8a8a;
  --card:#f6f6f6;
  --night:#1b1b1d;
  --field:#3a3a3c;
  --line:#d9d9d9;
  --sky-1:#141b2a;
  --sky-2:#2b3241;
  --folk:#4d4a9e;
  --chirp:#5aaedc;
  --globe:#e5533b;
}
*{box-sizing:border-box;margin:0;padding:0}
html,body{width:1200px;height:2562px;overflow:hidden}
body{font-family:"Exo 2",sans-serif;color:var(--ink);background:var(--white);position:relative}
.abs{position:absolute}
.btn{position:absolute;display:flex;align-items:center;justify-content:center;background:var(--blue-btn);color:var(--white);font-weight:600;font-size:13px;letter-spacing:.5px;text-transform:uppercase;text-decoration:none}

/* hero */
.hero{position:absolute;left:0;top:0;width:1200px;height:646px;background:radial-gradient(ellipse at 70% 20%,#3a4152 0%,transparent 55%),linear-gradient(180deg,var(--sky-2) 0%,var(--sky-1) 55%,#0b0d12 100%)}
.hero-photo{position:absolute;inset:0}
.topbar-phone{left:173px;top:31px;display:flex;align-items:center;gap:12px;color:var(--white);font-size:11px}
.topbar-phone .ico{width:32px;height:40px;background:var(--blue-btn);display:flex;align-items:center;justify-content:center}
.topbar-phone b{font-size:13px;font-weight:500}
.socials-top{right:173px;top:39px;display:flex}
.socials-top span{width:42px;height:26px;border-left:1px solid rgba(255,255,255,.2);display:flex;align-items:center;justify-content:center}
.socials-top span i{width:8px;height:8px;border-radius:50%;background:rgba(255,255,255,.6)}
.nav{top:142px;height:46px;display:flex;align-items:center;border-top:1px solid rgba(255,255,255,.2);border-bottom:1px solid rgba(255,255,255,.2);color:var(--white);font-size:13px}
.nav a{padding:0 18px;border-right:1px solid rgba(255,255,255,.25);line-height:16px;text-decoration:none;color:inherit;white-space:nowrap}
.nav a:last-child{border-right:none}
.nav-left{left:173px;width:340px}
.nav-right{left:688px;width:340px;justify-content:space-between}
.nav-right a{padding:0 13px}
.nav-left a:first-child{color:#5aa3e6;padding-left:14px;position:relative}
.nav-left a:first-child::after{content:"";position:absolute;left:0;right:12px;bottom:-16px;height:2px;background:#5aa3e6}
.logo{left:514px;top:78px;width:172px;height:172px;border-radius:50%;background:#0b0e16;border:3px solid rgba(255,255,255,.85);display:flex;align-items:center;justify-content:center;color:var(--white);font-size:26px;font-weight:500;line-height:1.05;text-align:center}
.arrow{top:294px;width:56px;height:56px;border-radius:50%;background:rgba(0,0,0,.55);border:1px solid rgba(255,255,255,.35);display:flex;align-items:center;justify-content:center}
.hero h1{left:0;width:1200px;top:306px;text-align:center;color:var(--white);font-weight:500;font-size:50px}
.hero h2{left:0;width:1200px;top:368px;text-align:center;color:var(--white);font-weight:300;font-size:48px;letter-spacing:1px}
.hero .rule{left:570px;top:442px;width:60px;height:2px;background:var(--blue)}
.dots{left:582px;top:596px;display:flex;gap:6px}
.dots i{width:8px;height:8px;border-radius:50%;border:1px solid rgba(255,255,255,.7)}
.dots i:first-child{background:var(--white)}

/* welcome */
.welcome-title{left:0;width:1200px;top:694px;text-align:center;font-size:30px;font-weight:300;letter-spacing:.5px}
.welcome-title b{font-weight:600}
.welcome-rule{left:560px;top:748px;width:80px;height:2px;background:var(--blue)}
.welcome-sub{left:0;width:1200px;top:766px;text-align:center;font-size:13px;color:#b9c8d8}
.card{top:875px;width:208px;height:188px;background:var(--card);text-align:center}
.card-icon{position:absolute;left:60px;top:-53px;width:88px;height:88px;border-radius:50%;background:var(--blue-btn);border:4px solid #e7edf5;display:flex;align-items:center;justify-content:center}
.card h3{position:absolute;left:0;right:0;top:59px;font-size:13px;font-weight:600}
.card p{position:absolute;left:18px;right:18px;top:91px;font-family:"Open Sans",sans-serif;font-size:10.5px;line-height:15px;color:var(--grey)}
.card .btn{left:58px;top:155px;width:90px;height:32px;font-size:11px}

/* caravan band */
.band{left:0;top:1211px;width:1200px;height:726px;background:var(--blue)}
.band-low{left:0;top:1590px;width:1200px;height:347px;background:var(--blue-deep)}
.band-title{left:0;width:1200px;top:1270px;text-align:center;color:var(--white);font-size:30px;font-weight:300}
.band-rule{left:560px;top:1318px;width:80px;height:2px;background:rgba(255,255,255,.6)}
.band-sub{left:0;width:1200px;top:1330px;text-align:center;color:var(--white);font-size:30px;font-weight:600}
.caravan{left:260px;top:1440px;width:690px;height:240px;border-radius:14px;background:linear-gradient(180deg,rgba(255,255,255,.32) 0%,rgba(255,255,255,.2) 60%,rgba(255,255,255,.1) 100%)}
.band-text{left:300px;width:600px;top:1750px;text-align:center;color:var(--white);font-family:"Open Sans",sans-serif;font-size:11.5px;line-height:19px}
.book{left:503px;top:1815px;width:192px;height:56px;background:var(--navy)}

/* contact strip */
.strip-col{top:1970px}
.strip-col h4{font-size:17px;font-weight:500;margin-bottom:14px}
.strip-col .val{display:flex;align-items:center;gap:12px;color:var(--blue);font-size:19px;white-space:nowrap}
.strip-col small{display:block;margin:6px 0 0 32px;font-size:11px;color:#aaa}
.strip-div{top:1965px;width:1px;height:100px;background:var(--line)}

/* footer */
.footer{left:0;top:2092px;width:1200px;height:392px;background:var(--night)}
.f-head{top:2152px;color:var(--blue);font-size:11px;font-weight:600;letter-spacing:.5px;border-bottom:1px solid #333;padding-bottom:8px}
.field{background:var(--field);color:#aaa;font-size:11px;padding:9px 10px;font-family:"Open Sans",sans-serif}
.send{background:var(--blue-btn);height:30px;font-size:10px}
.blog-item{left:383px;width:212px;height:48px;display:flex;gap:14px}
.blog-thumb{width:48px;height:44px;flex:none;background:linear-gradient(160deg,#3d5f9c,#0d1526)}
.blog-item h5{color:var(--blue);font-size:11px;font-weight:600}
.blog-item p{color:#999;font-size:9.5px;font-family:"Open Sans",sans-serif;line-height:13px}
.blog-item b{color:var(--white);font-size:9px}
.special{left:575px;top:2168px;width:452px;height:0}
.special-photo{left:576px;top:2193px;width:250px;height:155px;background:linear-gradient(180deg,#c7512c 0%,#e77a35 45%,#f3a64a 62%,#2a1715 100%)}
.ribbon{left:758px;top:2193px;width:66px;height:82px;background:var(--blue-btn);clip-path:polygon(0 0,100% 0,100% 100%,50% 84%,0 100%);color:var(--white);font-size:11px;font-weight:700;text-align:center;padding-top:12px;line-height:14px}
.social{top:2391px;height:38px;display:flex;align-items:center;color:var(--white);font-size:10px;letter-spacing:.5px}
.social .sq{width:42px;height:100%;display:flex;align-items:center;justify-content:center;border-right:1px solid rgba(255,255,255,.25)}
.social .sq i{width:10px;height:10px;background:var(--white)}
.social .name{flex:1;text-align:center;border-right:1px solid rgba(255,255,255,.25);line-height:38px}
.social .count{width:86px;text-align:center}
.copy{left:0;top:2484px;width:1200px;height:78px;display:flex;align-items:center;justify-content:center;gap:14px;font-size:12px;color:#555}
.copy .mark{width:28px;height:28px;border-radius:50%;background:var(--blue-btn)}
</style>
</head>
<body>

<header class="hero">
  <div class="hero-photo" role="img" aria-label="Night sky over the Kimberley with a portable telescope on a tripod beside a parked car"></div>
  <div class="abs topbar-phone"><span class="ico"><svg width="14" height="14" viewBox="0 0 24 24"><path fill="#fff" d="M6.6 10.8a15 15 0 0 0 6.6 6.6l2.2-2.2a1 1 0 0 1 1-.25 11.4 11.4 0 0 0 3.6.57 1 1 0 0 1 1 1V20a1 1 0 0 1-1 1A17 17 0 0 1 3 4a1 1 0 0 1 1-1h3.5a1 1 0 0 1 1 1c0 1.25.2 2.45.57 3.57a1 1 0 0 1-.25 1z"/></svg></span><span>Any Questions? Call Us: <b>0800 (555) 0190</b></span></div>
  <div class="abs socials-top"><span><i></i></span><span><i></i></span><span><i></i></span><span><i></i></span></div>
  <nav class="abs nav nav-left"><a>Home</a><a>Astronomy Events</a><a>Tours</a></nav>
  <nav class="abs nav nav-right"><a>Calendar</a><a>Gallery</a><a>Testimonials</a><a>Contacts</a></nav>
  <div class="abs logo">Quandoria<br>Tours</div>
  <div class="abs arrow" style="left:54px"><svg width="14" height="14" viewBox="0 0 14 14"><path d="M9 2 4 7l5 5" stroke="#fff" stroke-width="2" fill="none"/></svg></div>
  <div class="abs arrow" style="left:1083px"><svg width="14" height="14" viewBox="0 0 14 14"><path d="m5 2 5 5-5 5" stroke="#fff" stroke-width="2" fill="none"/></svg></div>
  <h1 class="abs">Travel With Us For The Best Deal !</h1>
  <h2 class="abs">Enjoy Wonderful Feelings !</h2>
  <div class="abs rule"></div>
  <a class="btn" style="left:505px;top:483px;width:190px;height:59px">Reach us today</a>
  <div class="abs dots"><i></i><i></i><i></i></div>
</header>

<section>
  <h2 class="abs welcome-title">WELCOME TO THE <b>QUANDORIA TOURS</b></h2>
  <div class="abs welcome-rule"></div>
  <p class="abs welcome-sub">Travel With Us For The Best Deal !</p>
  <div class="abs card" style="left:173px"><div class="card-icon"><svg width="40" height="40" viewBox="0 0 40 40"><path d="M8 20 30 10l3 6-22 10z" fill="#fff"/><path d="M20 22l-6 14M20 22l6 14M20 22v14" stroke="#fff" stroke-width="2"/></svg></div><h3>QUANDORIA TOURS</h3><p>Night tours under clear outback skies, with guides and gear ready for you to look.</p><a class="btn">More</a></div>
  <div class="abs card" style="left:388px"><div class="card-icon"><svg width="40" height="40" viewBox="0 0 40 40"><circle cx="20" cy="20" r="12" stroke="#fff" stroke-width="2" fill="none"/><circle cx="20" cy="20" r="4" fill="#fff"/></svg></div><h3>QUANDORIA TOURS</h3><p>Night tours under clear outback skies, with guides and gear ready for you to look.</p><a class="btn">More</a></div>
  <div class="abs card" style="left:603px"><div class="card-icon"><svg width="44" height="40" viewBox="0 0 44 40"><rect x="6" y="10" width="30" height="18" rx="6" fill="#fff"/><circle cx="18" cy="30" r="4" fill="#fff" stroke="#2b63ae" stroke-width="2"/><path d="M36 24h6" stroke="#fff" stroke-width="2"/></svg></div><h3>QUANDORIA TOURS</h3><p>Night tours under clear outback skies, with guides and gear ready for you to look.</p><a class="btn">More</a></div>
  <div class="abs card" style="left:818px"><div class="card-icon"><svg width="40" height="40" viewBox="0 0 40 40"><circle cx="20" cy="20" r="12" stroke="#fff" stroke-width="2" fill="none"/><circle cx="20" cy="20" r="4" fill="#fff"/></svg></div><h3>QUANDORIA TOURS</h3><p>Night tours under clear outback skies, with guides and gear ready for you to look.</p><a class="btn">More</a></div>
  <a class="btn" style="left:503px;top:1103px;width:194px;height:57px">See more services</a>
</section>

<section>
  <div class="abs band"></div>
  <div class="abs band-low"></div>
  <h2 class="abs band-title">TOURISTS TO THE KIMBERLEY SUCH AS</h2>
  <div class="abs band-rule"></div>
  <h3 class="abs band-sub">CARAVAN TRAILERS</h3>
  <div class="abs caravan" role="img" aria-label="White touring caravan trailer shown in side view"></div>
  <p class="abs band-text">Lorem ipsum dolor sit amet, consecr adipiscing elit, sed diam nonummy nibh euismod ti to themsa me Lorem ipsum dolor sit amet, consecr adipiscing elit, sed diam nonummy nibh euismod ti to themsa me...</p>
  <a class="btn book">Book now !</a>
</section>

<section>
  <div class="abs strip-col" style="left:173px"><h4>Book by Phone !</h4><div class="val"><svg width="20" height="20" viewBox="0 0 24 24"><path fill="#3377b5" d="M6.6 10.8a15 15 0 0 0 6.6 6.6l2.2-2.2a1 1 0 0 1 1-.25 11.4 11.4 0 0 0 3.6.57 1 1 0 0 1 1 1V20a1 1 0 0 1-1 1A17 17 0 0 1 3 4a1 1 0 0 1 1-1h3.5a1 1 0 0 1 1 1c0 1.25.2 2.45.57 3.57a1 1 0 0 1-.25 1z"/></svg>1-555-014-2290</div><small>Booking time : 24 / 7 hours</small></div>
  <div class="abs strip-div" style="left:395px"></div>
  <div class="abs strip-col" style="left:443px"><h4>Give your Feedback !</h4><div class="val"><svg width="22" height="20" viewBox="0 0 24 20"><path d="M2 2h20v14H2z" fill="none" stroke="#3377b5" stroke-width="2"/><path d="m2 2 10 8 10-8" fill="none" stroke="#3377b5" stroke-width="2"/></svg>mail@quandoria.com</div><small>Help us improve</small></div>
  <div class="abs strip-div" style="left:725px"></div>
  <div class="abs strip-col" style="left:773px"><h4>Services and Support !</h4><div class="val"><svg width="20" height="20" viewBox="0 0 24 24"><path d="M4 14v-2a8 8 0 0 1 16 0v2" fill="none" stroke="#3377b5" stroke-width="2"/><rect x="2" y="13" width="5" height="7" fill="#3377b5"/><rect x="17" y="13" width="5" height="7" fill="#3377b5"/></svg>Support &amp; Service Centre</div><small>Get your doubts cleared</small></div>
</section>

<footer>
  <div class="abs footer"></div>
  <div class="abs f-head" style="left:173px;width:279px">CONTACT US</div>
  <div class="abs field" style="left:173px;top:2195px;width:135px;height:32px">Name</div>
  <div class="abs field" style="left:317px;top:2195px;width:135px;height:32px">Email</div>
  <div class="abs field" style="left:173px;top:2234px;width:279px;height:76px">Message</div>
  <a class="btn send" style="left:173px;top:2318px;width:279px">Send</a>

  <div class="abs f-head" style="left:383px;width:0;border:0"></div>
  <div class="abs f-head" style="left:518px;width:212px">BLOG</div>
  <div class="abs blog-item" style="left:518px;top:2193px"><div class="blog-thumb" role="img" aria-label="Night sky photo"></div><div><h5>QUANDORIA TOURS</h5><p>Lorem ipsum dolor sit amet...</p><b>MORE</b></div></div>
  <div class="abs blog-item" style="left:518px;top:2246px"><div class="blog-thumb" role="img" aria-label="Night sky photo"></div><div><h5>QUANDORIA TOURS</h5><p>Lorem ipsum dolor sit amet...</p><b>MORE</b></div></div>
  <div class="abs blog-item" style="left:518px;top:2299px"><div class="blog-thumb" role="img" aria-label="Night sky photo"></div><div><h5>QUANDORIA TOURS</h5><p>Lorem ipsum dolor sit amet...</p><b>MORE</b></div></div>

  <div class="abs f-head" style="left:779px;width:250px">SPECIAL</div>
  <div class="abs special-photo" style="left:779px" role="img" aria-label="Sunset sky with a stargazer silhouetted beside a telescope"></div>
  <div class="abs ribbon" style="left:943px">SPECIAL<br>OFFER<br>!!!</div>

  <div class="abs social" style="left:173px;width:265px;background:var(--folk)"><span class="sq"><i></i></span><span class="name">FOLKPAGE</span><span class="count">100k + LIKES</span></div>
  <div class="abs social" style="left:469px;width:266px;background:var(--chirp)"><span class="sq"><i style="border-radius:50%"></i></span><span class="name">CHIRPER</span><span class="count">100k + POSTS</span></div>
  <div class="abs social" style="left:764px;width:265px;background:var(--globe)"><span class="sq"><i></i></span><span class="name">GLOBE+</span><span class="count">100k + PLUS</span></div>

  <div class="abs copy"><span class="mark"></span><span>Copyrights © <b>Quandoria-Tours</b> 2015. All Rights Reserved. Privacy Policy</span></div>
</footer>

</body>
</html>
```